I'm doing a recreational cannabis grow business here in the Columbia Gorge scenic area . I'm looking for a business card similar to the Tarvelle Lodge logo,except for the sun raise to be pot leafs.
The Gorge mountains,the river with the sun coming off the water between the mountains with the pot leaf rays.
All print would be on the back side
Kick ass simple black and gold or kick ass colorful

Target Market(s)

Retailers

Industry/Entity Type

Business

Contact Information for Business Card

Lofty Fern
In the heart of the Columbia River Gorge
Email loftyfernllc@pinemail.net

Font styles to use
Other font styles liked:
• What the artist thinks

Colors

Designer to choose colors to be used in the design.

Requirements
Must have
• Nice to look at . Like that bottle of wine you buy because the label graphics told you too.
Nice to have
• It's in my description
• You can lookup the Tarvelle Logde in Stevenson Wa and check out there logo, and I'm always up for ideas.
• Color and fonts should be what the artist thinks best
Should not have
• Boring

```html
<!DOCTYPE html>
<html lang="en">
<head>
<meta charset="utf-8">
<title>Lofty Fern — Business Card</title>
<link rel="stylesheet" href="https://fonts.googleapis.com/css2?family=Open+Sans:wght@400;600;700&display=swap">
<style>
  :root {
    --page: #e9e9e7;
    --card: #f4f4f3;
    --green: #8cc63f;
    --green-light: #b5dc6a;
    --green-deep: #3f8f4e;
    --slate: #34454d;
    --grey-text: #5a6166;
    --white: #ffffff;
  }
  * { box-sizing: border-box; margin: 0; padding: 0; }
  html, body { width: 1200px; height: 800px; overflow: hidden; }
  body {
    background: var(--page);
    font-family: "Open Sans", Arial, sans-serif;
    position: relative;
  }
  .card {
    position: absolute;
    top: 245px;
    width: 540px;
    height: 310px;
    background: var(--card);
    box-shadow: 0 6px 18px rgba(0,0,0,0.12);
    overflow: hidden;
  }
  .card--front { left: 40px; }
  .card--back { left: 620px; }
  .card__art { position: absolute; inset: 0; }

  .brand {
    position: absolute;
    display: flex;
    align-items: center;
    gap: 12px;
  }
  .brand__dot {
    width: 26px; height: 26px;
    border-radius: 50%;
    background: var(--green);
  }
  .brand__name {
    font-weight: 700;
    font-size: 34px;
    color: var(--green-deep);
    letter-spacing: 0.5px;
    white-space: nowrap;
  }
  .card--front .brand { left: 50%; top: 50%; transform: translate(-50%, -50%); }
  .card--back .brand { left: 34px; top: 134px; }
  .card--back .brand__name { font-size: 28px; }
  .card--back .brand__dot { width: 22px; height: 22px; }

  .nameplate {
    position: absolute;
    left: 360px; top: 56px;
    width: 180px; height: 58px;
    padding-left: 30px;
    display: flex; flex-direction: column; justify-content: center;
  }
  .nameplate__name {
    font-weight: 600; font-size: 20px;
    color: var(--green); letter-spacing: 1px; line-height: 1.1;
  }
  .nameplate__role {
    font-size: 11px; color: var(--grey-text);
    letter-spacing: 3px; margin-top: 2px;
  }

  .contact {
    position: absolute;
    left: 372px; top: 150px;
    list-style: none;
    color: var(--white);
    font-size: 11.5px;
    line-height: 1.35;
  }
  .contact__item { display: flex; gap: 8px; margin-bottom: 7px; }
  .contact__icon { width: 12px; height: 12px; flex: none; margin-top: 2px; }
</style>
</head>
<body>

<section class="card card--front" aria-label="Card front">
  <svg class="card__art" viewBox="0 0 540 310" aria-hidden="true">
    <rect x="0" y="0" width="540" height="14" fill="var(--green)"/>
    <rect x="0" y="14" width="540" height="3" fill="var(--white)"/>
    <polygon points="0,284 300,284 300,296 0,296" fill="var(--green)"/>
    <polygon points="300,284 540,284 540,296 300,296" fill="var(--slate)"/>
  </svg>
  <div class="brand">
    <span class="brand__dot"></span>
    <span class="brand__name">Lofty Fern</span>
  </div>
</section>

<section class="card card--back" aria-label="Card back">
  <svg class="card__art" viewBox="0 0 540 310" aria-hidden="true">
    <defs>
      <linearGradient id="panelShade" x1="0" y1="0" x2="1" y2="0">
        <stop offset="0" stop-color="var(--green-light)"/>
        <stop offset="1" stop-color="var(--green)"/>
      </linearGradient>
    </defs>
    <polygon points="300,0 540,0 540,310 350,310" fill="#dff0c4"/>
    <polygon points="330,0 540,0 540,310 380,310" fill="url(#panelShade)"/>
    <line x1="322" y1="0" x2="372" y2="310" stroke="var(--green-deep)" stroke-width="3"/>
    <polygon points="360,56 540,56 540,114 360,114 380,85" fill="var(--white)"/>
  </svg>

  <div class="brand">
    <span class="brand__dot"></span>
    <span class="brand__name">Lofty Fern</span>
  </div>

  <div class="nameplate">
    <span class="nameplate__name">MARA ELLISON</span>
    <span class="nameplate__role">DIRECTOR</span>
  </div>

  <ul class="contact">
    <li class="contact__item">
      <svg class="contact__icon" viewBox="0 0 12 12" aria-hidden="true"><rect x="3" y="0.5" width="6" height="11" rx="1.2" fill="none" stroke="#fff" stroke-width="1.2"/><circle cx="6" cy="9.3" r="0.8" fill="#fff"/></svg>
      <span>09 555 0142</span>
    </li>
    <li class="contact__item">
      <svg class="contact__icon" viewBox="0 0 12 12" aria-hidden="true"><rect x="0.6" y="2" width="10.8" height="8" fill="none" stroke="#fff" stroke-width="1.2"/><polyline points="0.6,2 6,6.5 11.4,2" fill="none" stroke="#fff" stroke-width="1.2"/></svg>
      <span>loftyfernllc@pinemail.net</span>
    </li>
    <li class="contact__item">
      <svg class="contact__icon" viewBox="0 0 12 12" aria-hidden="true"><polygon points="6,0.8 11.5,5.8 10,5.8 10,11 2,11 2,5.8 0.5,5.8" fill="#fff"/></svg>
      <span>48 kauri ridge road west harbour<br>auckland 0618</span>
    </li>
  </ul>
</section>

</body>
</html>
```